Business Card Re-Design/Update

We'd like to update out business cards. I've included our current "Style guide" which has the colour scheme of the organisation in it. I've also included the branding files with logos etc in them.

I've also included a copy of one of our existing cards so that you can see how ugly/dated they look. I'd like a fresh modern corporate look.

Target Market(s)

These are for our clients, potential clients, industry contacts - like all business cards

Contact Information for Business Card

Name
Position
Company Address - Level 1, 47 Garnet Lane, Toowong Qld 4066
Direct Phone
mobile
Email
Website -www.korvalnet.com.au
Logo

Colors

Designer to choose colors to be used in the design.

Requirements
Must have
• Main Logo
• Cards will need to be editable to be able to personalize them for each new employee.
Nice to have
• The MapOUT, HandOVER, UpKEEP would be okay to have if they can be sensibly and professionally added to the look without detracting from the main imagery.
• Maybe they could go on the back of the card? will leave this to your creative discretion as to whether/where they fit.
Should not have
• Should not have decorative or script fonts

```html
<!DOCTYPE html>
<html lang="en">
<head>
<meta charset="utf-8">
<title>korvalNET Business Card – Front and Back</title>
<link rel="stylesheet" href="https://fonts.googleapis.com/css2?family=Montserrat:wght@400;500;600&family=Roboto+Condensed:wght@700&display=swap">
<style>
  :root {
    --stage: #e6e6e6;
    --stage-light: #f4f4f4;
    --card-red: #d81c24;
    --card-red-deep: #c9161f;
    --ink-white: #ffffff;
    --rule-gold: #e7a77a;
    --card-shadow: rgba(0, 0, 0, 0.18);
  }
  * { box-sizing: border-box; margin: 0; padding: 0; }
  html, body {
    width: 1200px;
    height: 1200px;
    overflow: hidden;
  }
  body {
    background: radial-gradient(circle at 50% 40%, var(--stage-light), var(--stage));
    font-family: "Montserrat", Arial, sans-serif;
    color: var(--ink-white);
    position: relative;
  }
  .card {
    position: absolute;
    left: 180px;
    width: 840px;
    height: 510px;
    border-radius: 3px;
    overflow: hidden;
    box-shadow: 0 14px 34px var(--card-shadow);
  }
  .card--front { top: 60px; }
  .card--back { top: 630px; }
  .card__texture {
    position: absolute;
    inset: 0;
    background: linear-gradient(135deg, var(--card-red) 0%, var(--card-red-deep) 100%);
  }
  .card__content {
    position: relative;
    height: 100%;
    display: flex;
    flex-direction: column;
    align-items: center;
  }
  .brand {
    display: flex;
    align-items: center;
    gap: 16px;
    font-weight: 600;
    letter-spacing: 0.5px;
  }
  .brand__mark {
    width: 34px;
    height: 34px;
    background: var(--ink-white);
  }
  .brand--front { margin-top: 70px; font-size: 46px; }
  .rule {
    height: 2px;
    background: linear-gradient(90deg, transparent, var(--rule-gold) 20%, var(--ink-white) 50%, var(--rule-gold) 80%, transparent);
  }
  .rule--front { width: 400px; margin: 26px 0 20px; }
  .holder__name { font-size: 34px; font-weight: 500; text-align: center; }
  .holder__role { font-size: 17px; font-weight: 400; text-align: center; margin-top: 8px; }
  .office { font-size: 16px; font-weight: 400; margin-top: 4px; }
  .rule--wide { width: 560px; margin: 20px 0 26px; }
  .contacts {
    display: flex;
    align-items: stretch;
    font-size: 15px;
    line-height: 1.45;
  }
  .contacts__group { padding: 0 22px; }
  .contacts__group + .contacts__group { border-left: 1.5px solid var(--ink-white); }
  .contacts__key { font-weight: 600; display: inline-block; width: 18px; }

  .brand--back { font-size: 86px; margin-top: 150px; gap: 28px; }
  .brand--back .brand__mark { width: 62px; height: 62px; }
  .taglines {
    position: absolute;
    bottom: 58px;
    left: 50%;
    transform: translateX(-50%);
    display: flex;
    flex-direction: column;
    align-items: center;
  }
  .rule--tag { width: 470px; }
  .taglines__row {
    display: flex;
    align-items: center;
    gap: 22px;
    padding: 12px 0;
    font-family: "Roboto Condensed", "Arial Narrow", sans-serif;
    font-weight: 700;
    font-size: 26px;
  }
  .taglines__sep { width: 2px; height: 22px; background: var(--ink-white); }
</style>
</head>
<body>

<section class="card card--front" aria-label="Business card front">
  <div class="card__texture" role="img" aria-label="Red card background with a faint tonal brand pattern"></div>
  <div class="card__content">
    <div class="brand brand--front">
      <span class="brand__mark" aria-hidden="true"></span>
      <span class="brand__name">korvalNET</span>
    </div>
    <div class="rule rule--front"></div>
    <p class="holder__name">Maren Holloway</p>
    <p class="holder__role">Business Development Manager</p>
    <div class="rule rule--front"></div>
    <p class="office">Level 1, 47 Garnet Lane, Toowong Qld 4066</p>
    <div class="rule rule--wide"></div>
    <div class="contacts">
      <div class="contacts__group">
        <p><span class="contacts__key">M</span> +61 (0)417 905 362</p>
        <p><span class="contacts__key">P</span> +61 (0)7 3870 4410</p>
      </div>
      <div class="contacts__group">
        <p><span class="contacts__key">D</span> +61 (0)7 3870 4427</p>
        <p><span class="contacts__key">F</span> +61 (0)7 3870 4499</p>
      </div>
      <div class="contacts__group">
        <p><span class="contacts__key">E</span> mholloway@korvalnet.com.au</p>
        <p><span class="contacts__key">W</span> www.korvalnet.com.au</p>
      </div>
    </div>
  </div>
</section>

<section class="card card--back" aria-label="Business card back">
  <div class="card__texture" role="img" aria-label="Red card background with a faint tonal brand pattern"></div>
  <div class="card__content">
    <div class="brand brand--back">
      <span class="brand__mark" aria-hidden="true"></span>
      <span class="brand__name">korvalNET</span>
    </div>
    <div class="taglines">
      <div class="rule rule--tag"></div>
      <div class="taglines__row">
        <span>The MapOUT</span>
        <span class="taglines__sep"></span>
        <span>HandOVER</span>
        <span class="taglines__sep"></span>
        <span>UpKEEP</span>
      </div>
      <div class="rule rule--tag"></div>
    </div>
  </div>
</section>

</body>
</html>
```